Business Card Design

Business card design.

Business card is to have logo, website address and email address.

Website is www.brightkettle.ie
Email is info@brightkettle.ie
Logo uploaded

I have ordered Business Card Printing via Print Harbor, the Double-sided colour printed option with gloss finish.

Industry/Entity Type

Business

```html
<!DOCTYPE html>
<html lang="en">
<head>
<meta charset="utf-8">
<title>BrightKettle.ie — Business Card</title>
<link rel="stylesheet" href="https://fonts.googleapis.com/css2?family=Nunito:wght@900&family=Archivo:wght@800&display=swap">
<style>
  :root {
    --backdrop: #9c9c9c;
    --card-light-top: #f2f2f2;
    --card-light-bottom: #c9caca;
    --ink: #000000;
    --brand-red: #ec2227;
    --label-bg: #f0eeee;
  }
  html, body {
    margin: 0;
    padding: 0;
    overflow: hidden;
  }
  .canvas {
    position: relative;
    width: 1200px;
    height: 1200px;
    background: var(--backdrop);
    overflow: hidden;
  }
  .card {
    position: absolute;
    left: 234px;
    width: 729px;
    height: 450px;
    overflow: hidden;
  }
  .card--front {
    top: 78px;
    background: linear-gradient(180deg, var(--card-light-top) 0%, var(--card-light-bottom) 100%);
  }
  .card--back {
    top: 622px;
    background: var(--ink);
  }
  .front-block {
    position: absolute;
  }
  .front-block--top {
    left: 246px;
    top: 0;
    width: 215px;
    height: 92px;
    background: var(--ink);
  }
  .front-block--bottom {
    left: 243px;
    bottom: 0;
    width: 216px;
    height: 100px;
    background: var(--brand-red);
  }
  .brand {
    position: absolute;
    left: 0;
    right: 0;
    top: 160px;
    display: flex;
    flex-direction: column;
    align-items: center;
  }
  .brand__dot {
    width: 66px;
    height: 66px;
    border-radius: 50%;
    background: var(--brand-red);
    margin-bottom: 10px;
  }
  .brand__name {
    font-family: "Nunito", sans-serif;
    font-weight: 900;
    font-size: 46px;
    line-height: 1;
    letter-spacing: -0.5px;
    color: var(--ink);
  }
  .back-disc {
    position: absolute;
    left: 474px;
    top: -20px;
    width: 280px;
    height: 280px;
    border-radius: 50%;
    background: var(--brand-red);
  }
  .contact-row {
    position: absolute;
    left: 0;
    width: 351px;
    height: 46px;
    background: var(--label-bg);
    display: flex;
    align-items: center;
    font-family: "Archivo", sans-serif;
    font-weight: 800;
    color: var(--brand-red);
  }
  .contact-row--web { top: 128px; }
  .contact-row--mail { top: 260px; }
  .contact-row__label {
    width: 153px;
    padding-left: 2px;
    font-size: 16px;
    letter-spacing: 0.3px;
  }
  .contact-row__value {
    font-size: 16px;
  }
</style>
</head>
<body>
<main class="canvas">
  <section class="card card--front" aria-label="Business card front">
    <div class="front-block front-block--top"></div>
    <div class="brand">
      <div class="brand__dot"></div>
      <div class="brand__name">BRIGHTKETTLE.IE</div>
    </div>
    <div class="front-block front-block--bottom"></div>
  </section>

  <section class="card card--back" aria-label="Business card back">
    <div class="back-disc"></div>
    <div class="contact-row contact-row--web">
      <span class="contact-row__label">WEBSITE</span>
      <span class="contact-row__value">www.brightkettle.ie</span>
    </div>
    <div class="contact-row contact-row--mail">
      <span class="contact-row__label">EMAIL</span>
      <span class="contact-row__value">info@brightkettle.ie</span>
    </div>
  </section>
</main>
</body>
</html>
```